Web-Based Software Platform - 34 Individual designs for user interface

We have a new piece of software that requires 34 individual "tiles" for a user interface. An example of the way they will be displayed is included in the file, along with examples of 34 tiles that we created in house.

There is a title associated with each tile. This is all real estate related.

image sizes needed

width: 290px
height: 218px

Target Market(s)

real estate users

Industry/Entity Type

Real Estate

Number of Pages Required

1 page

Font styles to use
Sans Serif

Colors
3176b5
fbee3d
9bcb3b
f37122

Requirements
Must have
• 34 seperate images
Nice to have
• see file
Should not have
• see file

```html
<!DOCTYPE html>
<html lang="en">
<head>
<meta charset="utf-8">
<title>Real Estate Data Tiles</title>
<link href="https://fonts.googleapis.com/css2?family=Vollkorn:wght@500&display=swap" rel="stylesheet">
<style>
  :root {
    --page-bg: #f5f5f5;
    --label: #1e1e1e;
    --red-a: #e42a26;
    --red-b: #ef3f35;
    --green-a: #31a51f;
    --green-b: #46b833;
    --orange-a: #f37a10;
    --orange-b: #f8901f;
    --circle: #ffffff;
  }
  * { box-sizing: border-box; margin: 0; padding: 0; }
  html, body { width: 1200px; height: 2586px; overflow: hidden; }
  body { background: var(--page-bg); position: relative; font-family: "Vollkorn", Georgia, serif; }

  .tile-card { position: absolute; width: 309px; }
  .tile {
    position: relative; width: 309px; height: 222px; overflow: hidden;
    display: flex; align-items: center; justify-content: center;
  }
  .tile::before {
    content: ""; position: absolute; inset: 0;
    background: linear-gradient(150deg, transparent 0 48%, rgba(255,255,255,.1) 48% 100%);
  }
  .tile::after {
    content: ""; position: absolute; left: 0; right: 0; bottom: 0; height: 60%;
    background: linear-gradient(180deg, transparent, rgba(0,0,0,.07));
  }
  .tile--buyer  { background: linear-gradient(135deg, var(--red-a), var(--red-b)); color: var(--red-a); }
  .tile--lender { background: linear-gradient(135deg, var(--green-a), var(--green-b)); color: var(--green-a); }
  .tile--export { background: linear-gradient(135deg, var(--orange-a), var(--orange-b)); color: var(--orange-a); }

  .tile-badge {
    position: relative; z-index: 1; width: 112px; height: 112px; border-radius: 50%;
    background: var(--circle); display: flex; align-items: center; justify-content: center;
  }
  .tile-badge svg { width: 54px; height: 54px; fill: none; stroke: currentColor; stroke-width: 2; stroke-linecap: round; stroke-linejoin: round; }

  .tile-label {
    margin-top: 16px; text-align: center; font-size: 16px; line-height: 29px;
    font-weight: 500; color: var(--label);
  }
</style>
</head>
<body>

<svg width="0" height="0" style="position:absolute">
  <defs>
    <symbol id="i-coin" viewBox="0 0 48 48"><circle cx="24" cy="24" r="9"/><path d="M27 20h-4a2 2 0 0 0 0 4h2a2 2 0 0 1 0 4h-4M24 17v3M24 28v3"/></symbol>
    <symbol id="i-house" viewBox="0 0 48 48"><path d="M6 24 22 10l16 14M10 21v17h18M17 38V28h8"/></symbol>
  </defs>
</svg>

<!-- Buyers -->
<figure class="tile-card" style="left:100px;top:133px">
  <div class="tile tile--buyer"><div class="tile-badge"><svg viewBox="0 0 48 48"><rect x="6" y="12" width="28" height="16" rx="1"/><rect x="10" y="17" width="28" height="16" rx="1"/><use href="#i-coin" x="14" y="13" width="22" height="22"/><path d="M30 36h14M30 39h14M30 42h14"/></svg></div></div>
  <figcaption class="tile-label">Active Cash Buyers</figcaption>
</figure>
<figure class="tile-card" style="left:447px;top:133px">
  <div class="tile tile--buyer"><div class="tile-badge"><svg viewBox="0 0 48 48"><path d="M12 8h16l4 4-4 4H12zM20 16v26M18 42h4"/><path d="M32 16l4 4v6M30 26h10l-2 16h-6z"/></svg></div></div>
  <figcaption class="tile-label">Fix N Flip Buyers</figcaption>
</figure>
<figure class="tile-card" style="left:791px;top:133px">
  <div class="tile tile--buyer"><div class="tile-badge"><svg viewBox="0 0 48 48"><path d="M6 18l8 2 10-8 4 1-6 9 9 3 4-3 3 1-3 5 2 5-3 1-4-3-9-1-4 10-4-1 2-11-8-4z"/><use href="#i-coin" x="22" y="22" width="26" height="26"/></svg></div></div>
  <figcaption class="tile-label">Out-Of-State Cash Buyers</figcaption>
</figure>
<figure class="tile-card" style="left:252px;top:465px">
  <div class="tile tile--buyer"><div class="tile-badge"><svg viewBox="0 0 48 48"><path d="M14 42V8h14v34M28 18h8v24M6 42h36M18 13h2M23 13h2M18 19h2M23 19h2M18 25h2M23 25h2M18 31h2M23 31h2M32 23h1M32 29h1M20 42v-6h4v6"/></svg></div></div>
  <figcaption class="tile-label">Commercial Cash Buyers</figcaption>
</figure>
<figure class="tile-card" style="left:598px;top:465px">
  <div class="tile tile--buyer"><div class="tile-badge"><svg viewBox="0 0 48 48"><path d="M6 24 42 8 32 40 22 28zM22 28l20-20M22 28l-2 10 6-6"/></svg></div></div>
  <figcaption class="tile-label">Wholesale Buyers</figcaption>
</figure>

<!-- Lenders -->
<figure class="tile-card" style="left:274px;top:841px">
  <div class="tile tile--lender"><div class="tile-badge"><svg viewBox="0 0 48 48"><use href="#i-house"/><use href="#i-coin" x="20" y="20" width="26" height="26"/></svg></div></div>
  <figcaption class="tile-label">Active Private Lenders</figcaption>
</figure>
<figure class="tile-card" style="left:619px;top:841px">
  <div class="tile tile--lender"><div class="tile-badge"><svg viewBox="0 0 48 48"><use href="#i-house" x="0" y="10" width="34" height="34"/><path d="M34 32V12M26 20l8-8 8 8"/><use href="#i-coin" x="6" y="26" width="18" height="18"/></svg></div></div>
  <figcaption class="tile-label">Private Lenders - Above $500k</figcaption>
</figure>
<figure class="tile-card" style="left:274px;top:1167px">
  <div class="tile tile--lender"><div class="tile-badge"><svg viewBox="0 0 48 48"><use href="#i-house" x="0" y="10" width="34" height="34"/><path d="M34 8v20M26 20l8 8 8-8"/><use href="#i-coin" x="6" y="26" width="18" height="18"/></svg></div></div>
  <figcaption class="tile-label">Private Lenders - Under $500k</figcaption>
</figure>
<figure class="tile-card" style="left:619px;top:1167px">
  <div class="tile tile--lender"><div class="tile-badge"><svg viewBox="0 0 48 48"><path d="M6 18l8 2 10-8 4 1-6 9 9 3 4-3 3 1-3 5 2 5-3 1-4-3-9-1-4 10-4-1 2-11-8-4z"/><use href="#i-coin" x="22" y="22" width="26" height="26"/></svg></div></div>
  <figcaption class="tile-label">Out-Of-State Private Lenders</figcaption>
</figure>

<!-- Exports & campaigns -->
<figure class="tile-card" style="left:100px;top:1540px">
  <div class="tile tile--export"><div class="tile-badge"><svg viewBox="0 0 48 48"><path d="M8 10h14l4 4v22H8zM16 16h14l4 4v22H16"/><path d="M32 6c6 0 8 4 8 8M37 11l3 3 3-3"/></svg></div></div>
  <figcaption class="tile-label">Data Export - Address Only</figcaption>
</figure>
<figure class="tile-card" style="left:447px;top:1540px">
  <div class="tile tile--export"><div class="tile-badge"><svg viewBox="0 0 48 48"><path d="M18 12h18v30H18zM22 18h10M22 23h10M22 28h10M22 33h6"/><path d="M12 14v18h4M10 30l-3 3 3 3M36 6h6v8M40 8l-6 6"/></svg></div></div>
  <figcaption class="tile-label">Data Export Address - Append<br>Phone, Email</figcaption>
</figure>
<figure class="tile-card" style="left:791px;top:1540px">
  <div class="tile tile--export"><div class="tile-badge"><svg viewBox="0 0 48 48"><path d="M6 20 24 8l18 12v20H6zM6 20l18 12 18-12M12 24V12h24v12M17 16h14M17 20h10"/><circle cx="36" cy="38" r="5"/></svg></div></div>
  <figcaption class="tile-label">Direct Mail - 3 Touch Campaign</figcaption>
</figure>

<figure class="tile-card" style="left:100px;top:1879px">
  <div class="tile tile--export"><div class="tile-badge"><svg viewBox="0 0 48 48"><path d="M6 20 24 8l18 12v20H6zM6 20l18 12 18-12M12 24V12h24v12M17 16h14M17 20h10"/><circle cx="26" cy="38" r="5"/></svg></div></div>
  <figcaption class="tile-label">Direct Mail - 5 Touch Campaign</figcaption>
</figure>
<figure class="tile-card" style="left:447px;top:1879px">
  <div class="tile tile--export"><div class="tile-badge"><svg viewBox="0 0 48 48"><path d="M10 6h20l8 8v28H10zM30 6v8h8M15 12h8"/><rect x="18" y="20" width="12" height="18" rx="2"/><path d="M22 34h4"/></svg></div></div>
  <figcaption class="tile-label">Data Export - Append Phone</figcaption>
</figure>
<figure class="tile-card" style="left:791px;top:1879px">
  <div class="tile tile--export"><div class="tile-badge"><svg viewBox="0 0 48 48"><path d="M12 6h20l8 8v28H12zM32 6v8h8M17 12h8"/><rect x="20" y="20" width="12" height="16" rx="2"/><circle cx="8" cy="38" r="3"/></svg></div></div>
  <figcaption class="tile-label">Data Export - Append Email</figcaption>
</figure>

<figure class="tile-card" style="left:274px;top:2200px">
  <div class="tile tile--export"><div class="tile-badge"><svg viewBox="0 0 48 48"><path d="M8 18h32v8H8zM11 26h26v16H11zM24 18v24M24 18c-4-8-12-8-10-2 1 2 6 2 10 2 4 0 9 0 10-2 2-6-6-6-10 2"/></svg></div></div>
  <figcaption class="tile-label">5 Touch Campaign - With<br>All Data Appends</figcaption>
</figure>
<figure class="tile-card" style="left:619px;top:2200px">
  <div class="tile tile--export"><div class="tile-badge"><svg viewBox="0 0 48 48"><path d="M16 10h26l-6 28H10zM19 16h16M18 21h16M17 26h12M6 18h6M4 24h7M6 30h4"/></svg></div></div>
  <figcaption class="tile-label">Custom Build Your<br>Direct Mail Campaign</figcaption>
</figure>

</body>
</html>
```